Quorvin Upcoming Gigs

One page graphic with my upcoming dates. Logo and photo attached, and sample from last flyer. Text:

QUORVIN

UPCOMING DATES

3/26/18 Tidal Plums (Las Vegas, NV)

4/1/18 Venture Hollow 2847 M St (Sac, CA)

4/8/18 Amber Heron (Sac, CA)

5/5/18 Low Ceiling @ Silver Moth (Sac, CA)

5/10/18 Pellman Art Museum (Sac, CA)

5/11/18 Vif Brume @ Cafe du Lierre (Sac, CA)

5/27/18 Sonnlicht JTR @ Vox (Sac, CA)

Save The Date: 9/21/18 Lanterns Festival (Puerto Nuevo, MX)

plazabook.example/quorvin482

Target Market(s)

House/Electronic Music

Industry/Entity Type

Night Club

Font styles to use
Sans Serif

Colors

Designer to choose colors to be used in the design.

Requirements
Must have
• Quorvin logo or something that looks good instead. Prefer photo to be in but not necessary.
Nice to have

```html
<!DOCTYPE html>
<html lang="en">
<head>
<meta charset="utf-8">
<title>Quorvin Upcoming Gigs</title>
<link rel="stylesheet" href="https://fonts.googleapis.com/css2?family=Montserrat:wght@900&family=Open+Sans:wght@600;700;800&display=swap">
<style>
  :root {
    --ink: #ffffff;
    --accent: #f6d21f;
    --night-deep: #0b0a1c;
    --night-violet: #3a2a6e;
    --night-blue: #1c2a5c;
    --night-magenta: #6b2350;
    --panel: rgba(6, 6, 14, 0.8);
  }
  * { margin: 0; padding: 0; box-sizing: border-box; }
  html, body { width: 849px; height: 1200px; overflow: hidden; background: var(--night-deep); }
  .flyer {
    position: relative;
    width: 849px;
    height: 1200px;
    overflow: hidden;
    font-family: "Open Sans", Arial, sans-serif;
    color: var(--ink);
  }
  .stage-photo {
    position: absolute;
    inset: 0;
    background:
      radial-gradient(ellipse at 80% 12%, rgba(120, 90, 200, 0.55), transparent 55%),
      radial-gradient(ellipse at 15% 40%, rgba(80, 70, 170, 0.45), transparent 60%),
      radial-gradient(ellipse at 75% 85%, rgba(140, 40, 90, 0.55), transparent 55%),
      linear-gradient(180deg, var(--night-violet) 0%, var(--night-blue) 45%, var(--night-deep) 75%, var(--night-magenta) 100%);
  }
  .wordmark {
    position: absolute;
    top: 40px;
    left: 0;
    width: 100%;
    text-align: center;
    font-family: "Montserrat", Arial, sans-serif;
    font-weight: 900;
    font-size: 112px;
    letter-spacing: 6px;
    line-height: 1;
  }
  .dates-frame { position: absolute; left: 0; top: 0; }
  .dates-panel {
    position: absolute;
    left: 104px;
    top: 260px;
    width: 642px;
    height: 790px;
    background: var(--panel);
  }
  .dates-heading {
    position: absolute;
    top: 318px;
    width: 100%;
    text-align: center;
    color: var(--accent);
    font-weight: 700;
    font-size: 42px;
    line-height: 1.2;
  }
  .gig-list {
    position: absolute;
    left: 136px;
    top: 410px;
    width: 600px;
    list-style: none;
  }
  .gig {
    font-weight: 600;
    font-size: 24px;
    line-height: 1.3;
    height: 89.5px;
    white-space: nowrap;
  }
  .gig-date { display: inline-block; width: 107px; }
  .gig-venue { color: var(--accent); }
  .save-date {
    position: absolute;
    top: 1090px;
    width: 100%;
    text-align: center;
    font-weight: 700;
    font-size: 20px;
  }
  .save-date .gig-place { color: var(--accent); }
  .social {
    position: absolute;
    top: 1142px;
    width: 100%;
    text-align: center;
    font-weight: 700;
    font-size: 21px;
  }
  .social-mark {
    display: inline-block;
    width: 20px;
    height: 20px;
    background: var(--ink);
    border-radius: 3px;
    vertical-align: -3px;
    margin-right: 10px;
  }
</style>
</head>
<body>
<main class="flyer">
  <div class="stage-photo" role="img" aria-label="Photo of the DJ performing behind the decks under purple club lights"></div>

  <h1 class="wordmark">QUORVIN</h1>

  <div class="dates-panel"></div>
  <svg class="dates-frame" width="849" height="1200" viewBox="0 0 849 1200" aria-hidden="true">
    <g stroke="#ffffff" stroke-width="2" fill="none">
      <line x1="80" y1="250" x2="770" y2="250"/>
      <line x1="80" y1="1060" x2="770" y2="1060"/>
      <line x1="94" y1="236" x2="94" y2="1074"/>
      <line x1="756" y1="236" x2="756" y2="1074"/>
    </g>
  </svg>

  <h2 class="dates-heading">UPCOMING DATES</h2>

  <ul class="gig-list">
    <li class="gig"><span class="gig-date">3/26/18</span><span class="gig-venue">Tidal Plums</span> (Las Vegas, NV)</li>
    <li class="gig"><span class="gig-date">4/1/18</span><span class="gig-venue">Venture Hollow 2847 M St</span> (Sac, CA)</li>
    <li class="gig"><span class="gig-date">4/8/18</span><span class="gig-venue">Amber Heron</span> (Sac, CA)</li>
    <li class="gig"><span class="gig-date">5/5/18</span><span class="gig-venue">Low Ceiling @ Silver Moth</span> (Sac, CA)</li>
    <li class="gig"><span class="gig-date">5/10/18</span><span class="gig-venue">Pellman Art Museum</span> (Sac, CA)</li>
    <li class="gig"><span class="gig-date">5/11/18</span><span class="gig-venue">Vif Brume @ Cafe du Lierre</span> (Sac, CA)</li>
    <li class="gig"><span class="gig-date">5/27/18</span><span class="gig-venue">Sonnlicht JTR @ Vox</span> (Sac, CA)</li>
  </ul>

  <p class="save-date">Save The Date: <span class="gig-place">9/21/18</span> Lanterns Festival <span class="gig-place">(Puerto Nuevo, MX)</span></p>

  <p class="social"><span class="social-mark"></span>plazabook.example/quorvin482</p>
</main>
</body>
</html>
```